Corporate Vision/Mission Designs for the Office Walls

What we are looking for:

We are looking for design proposals to frame our mission, vision and values on our office walls

The designs need to be elegant, clean lines, simple, easy to follow and of course, should follow our brand guidelines.

Here's the copy:

For Boardoom:
Vision: Marlow Prestwick ignites people with passion enabling joy and lifetime memories

Mission: We are transforming the way property is bought.

For Garage
Purpose: We connect people with their dreams, turn dreams into reality.

For Entrance
Core Values
Honour
Passion
Sharing
Surprise
Fun

Vision & Mission will go in the boardroom
Core Values : at the Entrance
Purpose: in the Garage meeting room

Attachments to this project include:

a) Photos of the walls where they will go, and the current designs on the walls

b) brand guidelines

Industry/Entity Type

Office

Font styles to use
Decorative

Requirements
Must have
• Follow the brandguidelines, and colors.
• Green / use minimally

```html
<!DOCTYPE html>
<html lang="en">
<head>
<meta charset="utf-8">
<title>Core Values – Entrance Wall</title>
<link rel="stylesheet" href="https://fonts.googleapis.com/css2?family=Alegreya+Sans:ital,wght@1,400&family=Tenor+Sans&display=swap">
<style>
  :root {
    --wall: #eeedeb;
    --teal: #1ab5ab;
    --ink: #55545b;
  }
  html, body {
    margin: 0;
    padding: 0;
    width: 900px;
    height: 1200px;
    overflow: hidden;
    background: var(--wall);
  }
  .wall-graphic {
    position: relative;
    width: 900px;
    height: 1200px;
  }
  .heading-marker {
    position: absolute;
    left: 280px;
    top: 270px;
    width: 14px;
    height: 52px;
    background: var(--teal);
  }
  .heading {
    position: absolute;
    left: 336px;
    top: 264px;
    margin: 0;
    font-family: "Alegreya Sans", "Optima", sans-serif;
    font-style: italic;
    font-weight: 400;
    font-size: 56px;
    line-height: 1;
    color: var(--teal);
    letter-spacing: 0.5px;
  }
  .values-list {
    position: absolute;
    left: 290px;
    top: 366px;
    margin: 0;
    padding: 0;
    list-style: none;
    font-family: "Tenor Sans", "Optima", sans-serif;
    font-size: 44px;
    line-height: 63.5px;
    color: var(--ink);
    letter-spacing: 0.5px;
  }
  .values-list li {
    height: 63.5px;
  }
  .accent-rule {
    position: absolute;
    left: 582px;
    top: 445px;
    width: 2px;
    height: 213px;
    background: var(--teal);
  }
</style>
</head>
<body>
  <main class="wall-graphic">
    <div class="heading-marker"></div>
    <h1 class="heading">Core Values</h1>
    <ul class="values-list">
      <li>HONOUR</li>
      <li>PASSION</li>
      <li>SHARING</li>
      <li>SURPRISE</li>
      <li>FUN</li>
    </ul>
    <div class="accent-rule"></div>
  </main>
</body>
</html>
```